NFC (Near field communication) - Business Card Design

IT/ Telecom:

We would like a new business card that contains our logo, contact info for the company and contact info for the owner. We also wolud like to be innovative, and create NFC technology inside the card.

This means that mobile phones can be placed on the card, and the contactinfo automaticly stores into the phonebook. Therefore, a cirkle or similar - with the text: "Place your phone here!" (please write it in Norwagian): "Aktiver NFC og legg mobilen din her!".

Please google NFC or near field communication and use your imagination on the design as we love surprises :-)

Industry/Entity Type

Communication

Requirements
Must have
• Text: "Activate NFC on your phone and place your mobile here - in Norwegian: "Aktiver NFC og legg mobilen din her!".
Nice to have
• Please see attachment #5 for inspiration.

```html
<!DOCTYPE html>
<html lang="no">
<head>
<meta charset="utf-8">
<title>Tellora – NFC visittkort</title>
<link rel="stylesheet" href="https://fonts.googleapis.com/css2?family=Lato:wght@400;700&display=swap">
<style>
  :root {
    --page-bg: #e8edf0;
    --slate: #5f8397;
    --slate-light: #7c9cae;
    --card-white: #ffffff;
    --text-grey: #3a3f44;
    --label-grey: #4a4f55;
    --shadow: rgba(30, 50, 60, 0.18);
  }
  * { box-sizing: border-box; margin: 0; padding: 0; }
  html, body {
    width: 1200px;
    height: 900px;
    overflow: hidden;
    background: var(--page-bg);
    font-family: "Lato", Arial, sans-serif;
  }
  .sheet {
    width: 1200px;
    height: 900px;
    display: flex;
    align-items: center;
    justify-content: center;
    gap: 60px;
  }
  .card {
    width: 525px;
    height: 300px;
    border-radius: 4px;
    box-shadow: 0 10px 30px var(--shadow);
    position: relative;
    overflow: hidden;
  }

  /* Back side – NFC tap zone */
  .card-back { background: var(--slate); }
  .nfc-zone {
    position: absolute;
    left: 132px;
    top: 40px;
    width: 261px;
    height: 200px;
    border-radius: 50%;
    background: radial-gradient(ellipse at center, var(--slate-light) 0%, var(--slate) 70%);
  }
  .nfc-mark {
    position: absolute;
    left: 50%;
    top: 120px;
    transform: translateX(-50%);
    width: 30px;
    height: 30px;
    background: #ffffff;
    border-radius: 3px;
  }
  .nfc-prompt {
    position: absolute;
    left: 0; right: 0;
    top: 236px;
    text-align: center;
    color: #ffffff;
    font-size: 14px;
    letter-spacing: 0.3px;
  }

  /* Front side – contact details */
  .card-front { background: var(--card-white); padding: 34px 40px 0 44px; }
  .brand {
    display: flex;
    align-items: center;
    gap: 14px;
    color: var(--slate);
    font-weight: 400;
    font-size: 44px;
    letter-spacing: -0.5px;
    line-height: 1;
  }
  .brand .mark {
    width: 46px; height: 32px; background: var(--slate); border-radius: 4px;
  }
  .person { margin-top: 30px; }
  .person-name { color: var(--slate); font-weight: 700; font-size: 17px; }
  .person-role { color: var(--label-grey); font-size: 12px; letter-spacing: 0.5px; margin-top: 2px; }
  .contact-list { list-style: none; margin-top: 16px; }
  .contact-list li {
    display: flex; align-items: center; gap: 14px;
    font-size: 14px; color: var(--text-grey); height: 19px;
  }
  .contact-list .icon {
    width: 12px; height: 12px; border-radius: 50%;
    background: var(--slate); color: #fff;
    font-size: 8px; font-weight: 700;
    display: flex; align-items: center; justify-content: center;
  }
  .contact-list .web { color: var(--slate); }
  .address { margin-top: 18px; font-size: 13px; color: var(--text-grey); }
  .address strong { color: var(--slate); font-weight: 700; }
</style>
</head>
<body>
<main class="sheet">
  <section class="card card-back" aria-label="Kortets bakside med NFC-sone">
    <div class="nfc-zone" role="img" aria-label="NFC-bølgemotiv rundt merket"></div>
    <span class="nfc-mark" aria-hidden="true"></span>
    <p class="nfc-prompt">Aktiver NFC og legg mobilen din her!</p>
  </section>

  <section class="card card-front" aria-label="Kortets forside med kontaktinformasjon">
    <div class="brand"><span class="mark"></span>tellora</div>
    <div class="person">
      <p class="person-name">Erik Halvorsen</p>
      <p class="person-role">DIRECTOR</p>
    </div>
    <ul class="contact-list">
      <li><span class="icon">t</span>+47 555 01 234</li>
      <li><span class="icon">e</span>erik@tellora.no</li>
      <li><span class="icon">w</span><span class="web">www.tellora.no</span></li>
    </ul>
    <p class="address"><strong>Tellora AS,</strong> Strandgata 12B, 0150 Oslo</p>
  </section>
</main>
</body>
</html>
```